Business Cards for an engineering & contracting company
Korvane Group
Business Cards for an engineering & contracting company - Architecture
Creative Brief
Professional
Architect Marwan Tarek Korvane
CEO - Project Manager
Chiyah, Blvd Rue Doumani, Next to Meridel Plaza, Korvane Tower, Blk B - 2nd floor
marwan@korvanegroup-example.com
www.korvanegroup-example.com
the word "Architect" can be written in a nice design before the name, The name is "Marwan Tarek Korvane". The company name is "Korvane Group" The country is " Beirut, Lebanon" Its preferable is the card is made of 2 or 3 colors that make it impressive
A design that is related to the company description, which is (architecture, engineering, design, contracting and construction) The logo may be a solution if its alone or with something else added to it.
Korvane Korvane
I'd like to see other stationery designs too in addition to the business card.

```html
<!DOCTYPE html>
<html lang="en">
<head>
<meta charset="utf-8">
<title>Korvane Group – Business Cards</title>
<link href="https://fonts.googleapis.com/css2?family=Cinzel:wght@600&family=Open+Sans:wght@400;600&display=swap" rel="stylesheet">
<style>
  :root {
    --backdrop: #e9e7e4;
    --card: #ffffff;
    --card-shade: #f2f2f2;
    --blue: #2f7fe0;
    --blue-dark: #1f5fb8;
    --grey: #8a8d91;
    --grey-light: #c9cbce;
    --ink: #4a4d52;
    --name-blue: #2a6fc9;
  }
  * { margin: 0; padding: 0; box-sizing: border-box; }
  html, body { width: 1200px; height: 828px; overflow: hidden; background: var(--backdrop); }
  .stage { position: relative; width: 1200px; height: 828px; }
  .card {
    position: absolute; top: 264px; width: 520px; height: 300px;
    background: linear-gradient(180deg, var(--card) 0%, var(--card-shade) 100%);
    box-shadow: 0 6px 18px rgba(0,0,0,0.18);
    overflow: hidden;
  }
  .card--front { left: 53px; }
  .card--back { left: 627px; }

  .brand { display: flex; align-items: center; gap: 10px; }
  .brand__square { width: 22px; height: 22px; background: var(--blue); }
  .brand__name {
    font-family: "Cinzel", serif; font-weight: 600; color: var(--blue-dark);
    letter-spacing: 1px; white-space: nowrap;
  }
  .brand__tagline {
    font-family: "Open Sans", sans-serif; letter-spacing: 1.5px;
    color: var(--grey); text-transform: uppercase; white-space: nowrap;
  }

  .card--front .brand-block {
    position: absolute; left: 0; right: 0; top: 112px;
    display: flex; flex-direction: column; align-items: center;
  }
  .card--front .brand__name { font-size: 30px; }
  .card--front .brand__tagline { font-size: 9px; margin-top: 6px; }

  .card--back .swoosh { position: absolute; inset: 0; }
  .card--back .brand-block { position: absolute; left: 40px; top: 150px; }
  .card--back .brand__square { width: 18px; height: 18px; }
  .card--back .brand__name { font-size: 21px; }
  .card--back .brand__tagline { font-size: 7px; margin-top: 5px; }

  .holder { position: absolute; left: 292px; top: 38px; font-family: "Open Sans", sans-serif; }
  .holder__name { font-size: 12px; font-weight: 600; color: var(--name-blue); text-transform: uppercase; letter-spacing: 0.4px; white-space: nowrap; }
  .holder__role { font-size: 9px; color: var(--ink); margin-top: 2px; }

  .contact { position: absolute; left: 292px; top: 84px; font-family: "Open Sans", sans-serif; font-size: 8px; color: var(--ink); }
  .contact__row { display: flex; align-items: flex-start; gap: 6px; margin-bottom: 5px; line-height: 1.35; white-space: nowrap; }
  .contact__row svg { flex: none; width: 9px; height: 9px; margin-top: 1px; }

  .web {
    position: absolute; right: 4px; bottom: 22px;
    writing-mode: vertical-rl; transform: rotate(180deg);
    font-family: "Open Sans", sans-serif; font-size: 7.5px; letter-spacing: 1px; color: #ffffff;
    white-space: nowrap;
  }
</style>
</head>
<body>
<main class="stage">

  <section class="card card--front" aria-label="Business card front">
    <div class="brand-block">
      <div class="brand">
        <span class="brand__square"></span>
        <span class="brand__name">KORVANE GROUP</span>
      </div>
      <p class="brand__tagline">Engineering &amp; Contracting Solutions</p>
    </div>
  </section>

  <section class="card card--back" aria-label="Business card back">
    <svg class="swoosh" viewBox="0 0 520 300" preserveAspectRatio="none" aria-hidden="true">
      <path d="M0 258 C220 246 420 206 502 58 L502 84 C430 220 220 266 0 272 Z" fill="var(--grey-light)"/>
      <path d="M0 300 L0 284 C230 276 430 236 502 100 L502 0 L520 0 L520 300 Z" fill="var(--blue)"/>
    </svg>

    <div class="brand-block">
      <div class="brand">
        <span class="brand__square"></span>
        <span class="brand__name">KORVANE GROUP</span>
      </div>
      <p class="brand__tagline">Engineering &amp; Contracting Solutions</p>
    </div>

    <div class="holder">
      <p class="holder__name">Marwan Tarek Korvane</p>
      <p class="holder__role">CEO - Project Manager</p>
    </div>

    <div class="contact">
      <div class="contact__row">
        <svg viewBox="0 0 10 10"><path d="M5 0.5a3.2 3.2 0 0 1 3.2 3.2C8.2 6.2 5 9.5 5 9.5S1.8 6.2 1.8 3.7A3.2 3.2 0 0 1 5 0.5Z" fill="var(--grey)"/><circle cx="5" cy="3.7" r="1.2" fill="#fff"/></svg>
        <span>Korvane Tower, Blk B - 2nd floor<br>Rue Doumani, Chiyah</span>
      </div>
      <div class="contact__row">
        <svg viewBox="0 0 10 10"><rect x="0.5" y="2" width="9" height="6" fill="var(--grey)"/><path d="M0.5 2 L5 5.5 L9.5 2" stroke="#fff" stroke-width="0.8" fill="none"/></svg>
        <span>marwan@korvanegroup-example.com</span>
      </div>
      <div class="contact__row">
        <svg viewBox="0 0 10 10"><path d="M2 0.8 L3.8 2.6 L2.8 3.8 C3.4 5.2 4.8 6.6 6.2 7.2 L7.4 6.2 L9.2 8 L8 9.2 C4.4 9 1 5.6 0.8 2 Z" fill="var(--grey)"/></svg>
        <span>01 234 5678</span>
      </div>
    </div>

    <p class="web">www.korvanegroup-example.com</p>
  </section>

</main>
</body>
</html>
```